ReDesign CBD Packaging Box with needed Details and Pizazzz!

I have 3 things that need to be accomplished for this project to be completed.
1- Each box contains CBD oil in values of 500mg, 1500mg and 2500mg. Each value as a flavor as well. We offer 4 "Flavors": Natural (flavorless), Mint, Dragonfruit and Watermelon in the 3 variants listed above. So need a box for each.
2- After reviewing the design recently, I decided I am not as happy as I thought. So, I am open to any modifications that may make is shine and spark that says "buy me" figuratively.
3- The box should be easy to identify in terms of the amount of CBD and flavor it is. Play with colors maybe where the swirl is white is it is 2500mg, and gray if 1500mg and dark gray for 500mg? Something like that as an example but I am sure you have better ideas than I .

So to summarize, need to update the box with all the wording and information required to be on the box.

I am attaching:
1)the text that should be on the box in case you need it
2) the logo,
3)a version that i tried to making called "dragon fruit tincture 1500mg",
4)the original design packaging called "soapy packaging".
5)the template I am supposed to use.

Target Market(s)

Health and Nutrition, Sports, Alternative Medicine, Elderly,

Industry/Entity Type

Retail online

Requirements
Must have
• clear writing with clear font
Nice to have
• some color or absence of black maybe.
Should not have
• unnecessary images or too busy

```html
<!DOCTYPE html>
<html lang="en">
<head>
<meta charset="utf-8">
<title>Lather Lane CBD Tincture Cartons</title>
<link rel="stylesheet" href="https://fonts.googleapis.com/css2?family=Bebas+Neue&family=Kaushan+Script&family=Lato:wght@400;700;900&display=swap">
<style>
:root{
  --ink:#0f1a14;
  --cut:#2a8fe6;
  --paper:#ffffff;
  --white:#ffffff;
  --mint:#1bb592;
  --mint-light:#a8efd6;
  --dragon:#a6488a;
  --dragon-light:#cf97bc;
}
*{margin:0;padding:0;box-sizing:border-box}
html,body{width:903px;height:1200px;overflow:hidden;background:var(--paper)}
.canvas{position:relative;width:903px;height:1200px;font-family:"Lato",sans-serif}
.box{position:absolute;left:0;width:903px;height:591px}
.box--mint{top:0;--accent:var(--mint);--accent-light:var(--mint-light)}
.box--dragon{top:591px;--accent:var(--dragon);--accent-light:var(--dragon-light)}
.base-wave{position:absolute;left:248px;top:405px;width:398px;height:51px;background:linear-gradient(90deg,var(--accent),var(--accent-light) 50%,var(--accent))}
.dieline{position:absolute;left:0;top:0}
.dieline .panel{fill:var(--ink);stroke:var(--cut);stroke-width:1}
.dieline .band{fill:var(--accent-light);stroke:var(--cut);stroke-width:1}
.dieline .fold{stroke:var(--cut);stroke-width:1}
.dieline .edge{fill:none;stroke:var(--cut);stroke-width:1}
.dieline .rule{stroke:var(--accent-light);stroke-width:1.2}
.dieline .ring{fill:none;stroke:var(--accent);stroke-width:1.6}
.dieline .ring-thin{fill:none;stroke:var(--white);stroke-width:.8}
.dieline .seal{fill:none;stroke:var(--white);stroke-width:.8}
.dieline .barcode-space{fill:var(--paper)}
.abs{position:absolute}
.brand{color:var(--white);font-weight:900;text-align:center;line-height:1;letter-spacing:.5px}
.brand--front{width:99px;font-size:15px}
.brand--lid{left:348px;top:84px;width:99px;font-size:11px;transform:rotate(180deg)}
.flavor{font-family:"Kaushan Script",cursive;color:var(--accent);text-align:center;width:99px;font-size:17px;line-height:1}
.spectrum{color:var(--white);font-size:8px;text-align:center;width:99px;letter-spacing:.3px}
.tincture{font-family:"Bebas Neue",sans-serif;color:var(--white);font-size:20px;text-align:center;width:99px;line-height:1}
.strength{width:87px;height:15px;background:var(--accent);color:var(--white);display:flex;align-items:center;justify-content:center;gap:2px;font-family:"Bebas Neue",sans-serif;font-size:12px;line-height:1}
.strength small{font-family:"Lato",sans-serif;font-size:5px;line-height:.95;display:inline-block}
.claim{width:34px;text-align:center;color:var(--white);font-size:4.8px;font-weight:700}
.claim svg{display:block;margin:0 auto 3px}
.certified{width:99px;text-align:center;color:var(--accent);font-size:9px;font-weight:700;letter-spacing:1.6px}
.volume{width:99px;text-align:center;color:var(--white);font-size:9px}
.side{left:253px;width:90px;color:var(--white);font-size:5.4px;line-height:1.15}
.side-title{font-family:"Kaushan Script",cursive;font-size:8.5px;text-align:center;margin-bottom:6px}
.side p{margin-bottom:7px}
.side b{font-weight:900}
.contact{text-align:center;font-size:4.6px}
.lot{font-size:4.2px}
.copy{left:451px;top:176px;width:92px;color:var(--white);font-size:7px;font-weight:700;line-height:1.32;text-align:justify}
.copy p+p{margin-top:7px}
.barcode-label{left:563px;width:67px;text-align:center;color:var(--ink);font-size:9px;line-height:1.1}
</style>
</head>
<body>
<div class="canvas">

  <section class="box box--mint" aria-label="Mint 2500 mg carton dieline">
    <div class="base-wave" role="img" aria-label="Decorative mint wave artwork along the carton base"></div>
    <svg class="dieline" width="903" height="591" viewBox="0 0 903 591" aria-hidden="true">
      <polygon class="panel" points="352,8 443,8 447,42 348,42"/>
      <rect class="panel" x="348" y="42" width="99" height="100"/>
      <polygon class="panel" points="254,95 348,95 348,142 248,142"/>
      <polygon class="panel" points="447,95 541,95 547,142 447,142"/>
      <rect class="band" x="248" y="142" width="398" height="11"/>
      <rect class="panel" x="248" y="153" width="398" height="252" style="stroke:none"/>
      <rect class="edge" x="248" y="153" width="398" height="303"/>
      <line class="rule" x1="248" y1="155.5" x2="646" y2="155.5"/>
      <line class="fold" x1="348" y1="142" x2="348" y2="456"/>
      <line class="fold" x1="447" y1="142" x2="447" y2="456"/>
      <line class="fold" x1="547" y1="142" x2="547" y2="456"/>
      <polygon class="panel" points="248,456 348,456 348,503 254,503"/>
      <polygon class="panel" points="447,456 547,456 541,503 447,503"/>
      <rect class="panel" x="547" y="456" width="99" height="99"/>
      <rect class="barcode-space" x="563" y="482" width="67" height="51"/>
      <polygon class="panel" points="547,555 646,555 642,590 552,590"/>
      <circle class="ring" cx="397" cy="92" r="22"/>
      <circle class="ring" cx="397" cy="205" r="29"/>
      <circle class="ring" cx="596" cy="205" r="29"/>
      <circle class="seal" cx="273" cy="301" r="8.5"/>
      <circle class="seal" cx="298" cy="301" r="8.5"/>
      <circle class="seal" cx="322" cy="301" r="8.5"/>
      <circle class="ring-thin" cx="265" cy="351" r="3.5"/>
    </svg>

    <div class="abs brand brand--lid">LATHER<br>LANE</div>

    <div class="abs side" style="top:177px">
      <div class="side-title">Dragon Fruit Tincture</div>
      <p><b>INGREDIENTS:</b> Organic Non-GMP Coconut Oil, Certified Vegan and Highest Quality Full Spectrum CBD, Natural Vegan Flavoring.</p>
      <p><b>DIRECTIONS:</b> Recommended dosage is 0.25mg CBD multiplied by your body weight in pounds on a daily basis.</p>
      <p><b>WARNINGS:</b> Contains Tree Nuts (Coconut); Consult your doctor before use; Discontinue use if any adverse reactions occur. Do not use if tamper seal is broken.</p>
    </div>
    <div class="abs side contact" style="top:323px"><b>CONTACT:</b><br>Lather Lane<br>Harbor Vale, CA 90000<br>(800) 555-0142<br>hello@latherlane.com</div>
    <div class="abs side lot" style="left:276px;top:349px">LOT #05M0510230A EXP 5/</div>

    <div class="abs brand brand--front" style="left:348px;top:197px">LATHER<br>LANE</div>
    <div class="abs flavor" style="left:348px;top:257px">Mint</div>
    <div class="abs spectrum" style="left:348px;top:286px">FULL SPECTRUM</div>
    <div class="abs tincture" style="left:348px;top:297px">CBD TINCTURE</div>
    <div class="abs strength" style="left:354px;top:321px">2500<small>MG<br>CBD</small>|&nbsp;45<small>MG CBD<br>PER ML</small></div>
    <div class="abs claim" style="left:361px;top:355px"><svg width="18" height="14" viewBox="0 0 18 14"><path d="M9,13 C3,12 2,6 4,3 C6,5 7,6 9,1 C11,6 12,5 14,3 C16,6 15,12 9,13 Z M9,4 V13" fill="none" stroke="#fff" stroke-width="1"/></svg>ALL NATURAL</div>
    <div class="abs claim" style="left:403px;top:355px"><svg width="18" height="14" viewBox="0 0 18 14"><path d="M8,13 C2,11 1,6 2,2 C6,3 9,7 8,13 Z M9,12 C10,6 13,3 17,2 C17,7 14,11 9,12 Z" fill="none" stroke="#fff" stroke-width="1"/></svg>VEGAN</div>
    <div class="abs certified" style="left:348px;top:385px">CERTIFIED</div>
    <div class="abs volume" style="left:348px;top:438px">2 fl oz. | 59.1471 mL</div>

    <div class="abs copy">
      <p>Lorem ipsum dolor sit amet, consectetur adipiscing elit, sed do eiusmod tempor incididunt ut labore et dolore magna aliqua. Ut enim ad minim veniam, quis nostrud exercitation ullamco laboris nisi ut aliquip ex ea commodo consequat. Duis aute irure dolor in reprehenderit in voluptate velit esse cillum dolore eu fugiat nulla pariatur. Excepteur sint occaecat cupidatat non proident, sunt in culpa qui officia deserunt</p>
      <p>mollit anim id est laborum.</p>
    </div>

    <div class="abs brand brand--front" style="left:547px;top:197px">LATHER<br>LANE</div>
    <div class="abs flavor" style="left:547px;top:257px">Mint</div>
    <div class="abs spectrum" style="left:547px;top:286px">FULL SPECTRUM</div>
    <div class="abs tincture" style="left:547px;top:297px">CBD TINCTURE</div>
    <div class="abs strength" style="left:553px;top:321px">2500<small>MG<br>CBD</small>|&nbsp;45<small>MG CBD<br>PER ML</small></div>
    <div class="abs claim" style="left:560px;top:355px"><svg width="18" height="14" viewBox="0 0 18 14"><path d="M9,13 C3,12 2,6 4,3 C6,5 7,6 9,1 C11,6 12,5 14,3 C16,6 15,12 9,13 Z M9,4 V13" fill="none" stroke="#fff" stroke-width="1"/></svg>ALL NATURAL</div>
    <div class="abs claim" style="left:602px;top:355px"><svg width="18" height="14" viewBox="0 0 18 14"><path d="M8,13 C2,11 1,6 2,2 C6,3 9,7 8,13 Z M9,12 C10,6 13,3 17,2 C17,7 14,11 9,12 Z" fill="none" stroke="#fff" stroke-width="1"/></svg>VEGAN</div>
    <div class="abs certified" style="left:547px;top:385px">CERTIFIED</div>
    <div class="abs volume" style="left:547px;top:438px">2 fl oz. | 59.1471 mL</div>

    <div class="abs barcode-label" style="top:497px">BARCODE<br>SPACE</div>
  </section>

  <section class="box box--dragon" aria-label="Dragon Fruit 2500 mg carton dieline">
    <div class="base-wave" role="img" aria-label="Decorative dragon fruit wave artwork along the carton base"></div>
    <svg class="dieline" width="903" height="591" viewBox="0 0 903 591" aria-hidden="true">
      <polygon class="panel" points="352,8 443,8 447,42 348,42"/>
      <rect class="panel" x="348" y="42" width="99" height="100"/>
      <polygon class="panel" points="254,95 348,95 348,142 248,142"/>
      <polygon class="panel" points="447,95 541,95 547,142 447,142"/>
      <rect class="band" x="248" y="142" width="398" height="11"/>
      <rect class="panel" x="248" y="153" width="398" height="252" style="stroke:none"/>
      <rect class="edge" x="248" y="153" width="398" height="303"/>
      <line class="rule" x1="248" y1="155.5" x2="646" y2="155.5"/>
      <line class="fold" x1="348" y1="142" x2="348" y2="456"/>
      <line class="fold" x1="447" y1="142" x2="447" y2="456"/>
      <line class="fold" x1="547" y1="142" x2="547" y2="456"/>
      <polygon class="panel" points="248,456 348,456 348,503 254,503"/>
      <polygon class="panel" points="447,456 547,456 541,503 447,503"/>
      <rect class="panel" x="547" y="456" width="99" height="99"/>
      <rect class="barcode-space" x="563" y="482" width="67" height="51"/>
      <polygon class="panel" points="547,555 646,555 642,590 552,590"/>
      <circle class="ring" cx="397" cy="92" r="22"/>
      <circle class="ring" cx="397" cy="205" r="29"/>
      <circle class="ring" cx="596" cy="205" r="29"/>
      <circle class="seal" cx="275" cy="301" r="8.5"/>
      <circle class="seal" cx="300" cy="301" r="8.5"/>
      <circle class="seal" cx="324" cy="301" r="8.5"/>
      <circle class="ring-thin" cx="267" cy="351" r="3.5"/>
    </svg>

    <div class="abs brand brand--lid">LATHER<br>LANE</div>

    <div class="abs side" style="left:255px;top:177px">
      <div class="side-title">Dragon Fruit Tincture</div>
      <p><b>INGREDIENTS:</b> Organic Non-GMP Coconut Oil, Certified Vegan and Highest Quality Full Spectrum CBD, Natural Vegan Flavoring.</p>
      <p><b>DIRECTIONS:</b> Recommended dosage is 0.25mg CBD multiplied by your body weight in pounds on a daily basis.</p>
      <p><b>WARNINGS:</b> Contains Tree Nuts (Coconut); Consult your doctor before use; Discontinue use if any adverse reactions occur. Do not use if tamper seal is broken.</p>
    </div>
    <div class="abs side contact" style="left:255px;top:323px"><b>CONTACT:</b><br>Lather Lane<br>Harbor Vale, CA 90000<br>(800) 555-0142<br>hello@latherlane.com</div>
    <div class="abs side lot" style="left:278px;top:349px">LOT #05M0510230A EXP 5/</div>

    <div class="abs brand brand--front" style="left:348px;top:197px">LATHER<br>LANE</div>
    <div class="abs flavor" style="left:348px;top:257px">Dragon Fruit</div>
    <div class="abs spectrum" style="left:348px;top:286px">FULL SPECTRUM</div>
    <div class="abs tincture" style="left:348px;top:297px">CBD TINCTURE</div>
    <div class="abs strength" style="left:354px;top:321px">2500<small>MG<br>CBD</small>|&nbsp;45<small>MG CBD<br>PER ML</small></div>
    <div class="abs claim" style="left:361px;top:355px"><svg width="18" height="14" viewBox="0 0 18 14"><path d="M9,13 C3,12 2,6 4,3 C6,5 7,6 9,1 C11,6 12,5 14,3 C16,6 15,12 9,13 Z M9,4 V13" fill="none" stroke="#fff" stroke-width="1"/></svg>ALL NATURAL</div>
    <div class="abs claim" style="left:403px;top:355px"><svg width="18" height="14" viewBox="0 0 18 14"><path d="M8,13 C2,11 1,6 2,2 C6,3 9,7 8,13 Z M9,12 C10,6 13,3 17,2 C17,7 14,11 9,12 Z" fill="none" stroke="#fff" stroke-width="1"/></svg>VEGAN</div>
    <div class="abs certified" style="left:348px;top:385px">CERTIFIED</div>
    <div class="abs volume" style="left:348px;top:438px">2 fl oz. | 59.1471 mL</div>

    <div class="abs copy" style="left:453px">
      <p>Lorem ipsum dolor sit amet, consectetur adipiscing elit, sed do eiusmod tempor incididunt ut labore et dolore magna aliqua. Ut enim ad minim veniam, quis nostrud exercitation ullamco laboris nisi ut aliquip ex ea commodo consequat. Duis aute irure dolor in reprehenderit in voluptate velit esse cillum dolore eu fugiat nulla pariatur. Excepteur sint occaecat cupidatat non proident, sunt in culpa qui officia deserunt</p>
      <p>mollit anim id est laborum.</p>
    </div>

    <div class="abs brand brand--front" style="left:547px;top:197px">LATHER<br>LANE</div>
    <div class="abs flavor" style="left:547px;top:257px">Dragon Fruit</div>
    <div class="abs spectrum" style="left:547px;top:286px">FULL SPECTRUM</div>
    <div class="abs tincture" style="left:547px;top:297px">CBD TINCTURE</div>
    <div class="abs strength" style="left:553px;top:321px">2500<small>MG<br>CBD</small>|&nbsp;45<small>MG CBD<br>PER ML</small></div>
    <div class="abs claim" style="left:560px;top:355px"><svg width="18" height="14" viewBox="0 0 18 14"><path d="M9,13 C3,12 2,6 4,3 C6,5 7,6 9,1 C11,6 12,5 14,3 C16,6 15,12 9,13 Z M9,4 V13" fill="none" stroke="#fff" stroke-width="1"/></svg>ALL NATURAL</div>
    <div class="abs claim" style="left:602px;top:355px"><svg width="18" height="14" viewBox="0 0 18 14"><path d="M8,13 C2,11 1,6 2,2 C6,3 9,7 8,13 Z M9,12 C10,6 13,3 17,2 C17,7 14,11 9,12 Z" fill="none" stroke="#fff" stroke-width="1"/></svg>VEGAN</div>
    <div class="abs certified" style="left:547px;top:385px">CERTIFIED</div>
    <div class="abs volume" style="left:547px;top:438px">2 fl oz. | 59.1471 mL</div>

    <div class="abs barcode-label" style="top:497px">BARCODE<br>SPACE</div>
  </section>

</div>
</body>
</html>
```